Business Card Design Project

We consult with hotels on setting rates and maximizing a revenue strategy

Industry/Entity Type

Business

Contact Information for Business Card

I am not sure what I want. Our company offers high level consulting to hotels around the country but we are also laid back. I would like something that is professional but also shows the laid back side

```html
<!DOCTYPE html>
<html lang="en">
<head>
<meta charset="utf-8">
<title>Harborline – Business Card</title>
<link href="https://fonts.googleapis.com/css2?family=Source+Sans+3:wght@400;600&display=swap" rel="stylesheet">
<style>
  :root {
    --page-bg: #e4e1de;
    --card-top: #f7f6f5;
    --card-bottom: #eeecea;
    --teal: #2f7d78;
    --ink: #2e2a27;
    --icon: #2f7d78;
  }
  * { margin: 0; padding: 0; box-sizing: border-box; }
  html, body {
    width: 1200px;
    height: 900px;
    overflow: hidden;
    background: var(--page-bg);
    font-family: "Source Sans 3", "Myriad Pro", sans-serif;
  }
  .card {
    position: absolute;
    left: 145px;
    top: 170px;
    width: 910px;
    height: 560px;
    border-radius: 26px;
    background: linear-gradient(180deg, var(--card-top), var(--card-bottom));
    box-shadow: 0 10px 30px rgba(0,0,0,0.12);
  }
  .contact-block {
    position: absolute;
    left: 452px;
    top: 66px;
    color: var(--ink);
  }
  .person-name {
    font-size: 34px;
    font-weight: 600;
    color: var(--teal);
    line-height: 1.1;
  }
  .person-title {
    font-size: 25px;
    font-weight: 400;
    margin-top: 8px;
  }
  .contact-list {
    list-style: none;
    margin-top: 36px;
  }
  .contact-list li {
    display: flex;
    align-items: center;
    font-size: 25px;
    line-height: 38px;
  }
  .contact-list svg {
    width: 18px;
    height: 18px;
    margin-right: 16px;
    fill: var(--icon);
    flex: none;
  }
  .brand {
    position: absolute;
    left: 30px;
    top: 430px;
    display: flex;
    align-items: center;
  }
  .brand-square {
    width: 56px;
    height: 56px;
    background: var(--teal);
    margin-right: 22px;
  }
  .brand-name {
    font-size: 64px;
    font-weight: 600;
    letter-spacing: 2px;
    color: var(--ink);
    line-height: 1;
  }
</style>
</head>
<body>
  <div class="card">
    <div class="contact-block">
      <div class="person-name">Nora Whitfield</div>
      <div class="person-title">Regional Revenue Manager</div>
      <ul class="contact-list">
        <li>
          <svg viewBox="0 0 24 24" aria-hidden="true"><path d="M6.6 10.8a15.1 15.1 0 0 0 6.6 6.6l2.2-2.2a1 1 0 0 1 1-.25 11.4 11.4 0 0 0 3.6.57 1 1 0 0 1 1 1V20a1 1 0 0 1-1 1A17 17 0 0 1 3 4a1 1 0 0 1 1-1h3.5a1 1 0 0 1 1 1c0 1.25.2 2.45.57 3.57a1 1 0 0 1-.25 1z"/></svg>
          555-014-2230
        </li>
        <li>
          <svg viewBox="0 0 24 24" aria-hidden="true"><rect x="2" y="8" width="20" height="14" rx="2"/><rect x="7" y="2" width="10" height="5" rx="1"/></svg>
          555-014-7781
        </li>
        <li>
          <svg viewBox="0 0 24 24" aria-hidden="true"><path d="M2 5h20v14H2z M2 5l10 8 10-8" /></svg>
          Nora@HarborlineRMS.com
        </li>
        <li>
          <svg viewBox="0 0 24 24" aria-hidden="true"><circle cx="12" cy="12" r="10"/></svg>
          www.HarborlineRMS.com
        </li>
      </ul>
    </div>
    <div class="brand">
      <div class="brand-square"></div>
      <div class="brand-name">HARBORLINE</div>
    </div>
  </div>
</body>
</html>
```